Hydraulics Company Business Card Design

Modern business card design for a hydraulics company.
Our company colours are - black, orange and white.
I would like the following contact details included-
Name
Position
Phone number
Email
Website
Street Address

I have attached our company logo.
I would like the back of the card white.

Thank you.

```html
<!DOCTYPE html>
<html lang="en">
<head>
<meta charset="utf-8">
<title>Riverbend Hydraulics – Business Card</title>
<link rel="stylesheet" href="https://fonts.googleapis.com/css2?family=Poppins:wght@400;600&display=swap">
<style>
  :root {
    --orange: #f7a11f;
    --black: #050505;
    --white: #ffffff;
    --ink: #222222;
    --stage: #2c3036;
  }
  * { box-sizing: border-box; margin: 0; padding: 0; }
  html, body {
    width: 1200px; height: 985px; overflow: hidden;
    background: var(--stage);
    font-family: "Poppins", sans-serif;
  }
  .sheet {
    position: relative; width: 1200px; height: 985px;
    display: flex; gap: 40px; align-items: center; justify-content: center;
  }
  .card {
    position: relative; width: 540px; height: 309px;
    background: var(--white); border-radius: 16px; overflow: hidden;
    box-shadow: 0 10px 30px rgba(0,0,0,.35);
  }
  .brand {
    position: absolute; color: var(--orange);
    font-weight: 600; line-height: 1.2; white-space: nowrap;
  }

  /* Front */
  .card-front .brand { right: 36px; top: 52px; font-size: 26px; }
  .id-panel {
    position: absolute; left: 0; top: 118px; width: 245px; height: 140px;
    background: var(--orange); color: var(--white);
    padding: 26px 24px 0 0; text-align: right;
  }
  .person-name { font-size: 17px; font-weight: 600; text-transform: uppercase; letter-spacing: .3px; }
  .person-role { font-size: 13px; font-weight: 400; margin-top: 2px; }
  .contact-panel {
    position: absolute; left: 245px; top: 168px; right: 0; height: 90px;
    background: var(--black); color: var(--white);
    padding: 10px 0 0 26px; list-style: none;
  }
  .contact-panel li {
    display: flex; align-items: center; gap: 10px;
    font-size: 13px; line-height: 23px;
  }
  .contact-icon { width: 15px; height: 15px; flex: none; }
  .address {
    position: absolute; left: 28px; bottom: 20px;
    font-size: 12.5px; color: var(--ink);
  }

  /* Back */
  .card-back .brand { left: 0; right: 0; top: 112px; text-align: center; font-size: 30px; }
  .back-web {
    position: absolute; left: 0; right: 0; top: 190px; text-align: center;
    font-size: 13px; letter-spacing: 6px; color: var(--ink);
  }
</style>
</head>
<body>
<main class="sheet">

  <section class="card card-front" aria-label="Card front">
    <p class="brand">Riverbend Hydraulics</p>

    <div class="id-panel">
      <p class="person-name">Lena R. Ortiz</p>
      <p class="person-role">Director</p>
    </div>

    <ul class="contact-panel">
      <li>
        <svg class="contact-icon" viewBox="0 0 16 16" aria-hidden="true">
          <circle cx="8" cy="8" r="8" fill="var(--orange)"/>
          <path d="M5.2 4.2l1.3-.2.8 1.8-.9.8a5 5 0 0 0 2.8 2.8l.8-.9 1.8.8-.2 1.3c-.1.5-.5.8-1 .7A6.4 6.4 0 0 1 4.5 5.2c-.1-.5.2-.9.7-1z" fill="var(--black)"/>
        </svg>
        +1 555-010-2040
      </li>
      <li>
        <svg class="contact-icon" viewBox="0 0 16 16" aria-hidden="true">
          <circle cx="8" cy="8" r="8" fill="var(--orange)"/>
          <rect x="4" y="5" width="8" height="6" rx="1" fill="var(--black)"/>
          <path d="M4.4 5.5L8 8.3l3.6-2.8" stroke="var(--orange)" stroke-width="1" fill="none"/>
        </svg>
        hello@riverbendhyd.com
      </li>
      <li>
        <svg class="contact-icon" viewBox="0 0 16 16" aria-hidden="true">
          <circle cx="8" cy="8" r="8" fill="var(--orange)"/>
          <circle cx="8" cy="8" r="4" fill="none" stroke="var(--black)" stroke-width="1.1"/>
          <path d="M4 8h8M8 4c-2 2.4-2 5.6 0 8M8 4c2 2.4 2 5.6 0 8" stroke="var(--black)" stroke-width="1" fill="none"/>
        </svg>
        www.riverbendhyd.com
      </li>
    </ul>

    <p class="address">480 Mill Creek Rd., Suite 210, Arizona 85001</p>
  </section>

  <section class="card card-back" aria-label="Card back">
    <p class="brand">Riverbend Hydraulics</p>
    <p class="back-web">www.riverbendhyd.com</p>
  </section>

</main>
</body>
</html>
```